custom carpentry, woodworking and home repair company needs logo design and business card design

Attention: I apologize but I just received notification from my state that I cannot use the company name that I originally submitted (Beyond The Bench). The new name will be Lumbrella We need a company logo and business card design for our new company based in the Hampton Roads area of Virginia. The company name is Lumbrella. The final design should give a first impression of true craftsmanship and attention to detail. We would like the card to include the company name, my name Derek Halloway (owner), phone number (757) 482-3175, website (lumbrella-shop.example) and email address (derek@lumbrella-shop.example). Everything else is up to your discretion. Thanks, have fun, and good luck.

Industry/Entity Type

Business

Contact Information for Business Card

See project description

Logo Text

see project description

Colors

Designer to choose colors to be used in the design.

```html
<!DOCTYPE html>
<html lang="en">
<head>
<meta charset="utf-8">
<title>Lumbrella Business Card</title>
<link href="https://fonts.googleapis.com/css2?family=Lato:wght@400;700;900&display=swap" rel="stylesheet">
<style>
  :root {
    --page-bg: #d8d2cb;
    --panel-top: #2a303b;
    --panel-mid: #3a4250;
    --panel-bottom: #272c36;
    --frost-light: #eceae8;
    --frost-mid: #d6d4d3;
    --frost-edge: #c4c2c2;
    --text-light: #e9e6e2;
    --text-muted: #c9c6c2;
    --brand-ink: #23262d;
    --silver: #c9ccd2;
  }
  * { margin: 0; padding: 0; box-sizing: border-box; }
  html, body { width: 1200px; height: 970px; overflow: hidden; }
  body {
    background: var(--page-bg);
    font-family: "Lato", sans-serif;
    position: relative;
  }
  .business-card {
    position: absolute;
    left: 80px; top: 189px;
    width: 1040px; height: 592px;
    border-radius: 28px;
    overflow: hidden;
    background: linear-gradient(160deg, var(--frost-light) 0%, var(--frost-mid) 55%, var(--frost-edge) 100%);
    box-shadow: 0 18px 40px rgba(0,0,0,0.18);
  }
  .card-shapes { position: absolute; inset: 0; }
  .contact-panel {
    position: absolute;
    left: 66px; top: 112px;
    color: var(--text-light);
  }
  .holder-name { font-size: 34px; font-weight: 700; line-height: 1; margin-left: 4px; }
  .holder-role { font-size: 25px; font-weight: 400; line-height: 1.1; color: var(--text-muted); }
  .postal-address {
    margin-top: 82px;
    font-size: 25px; line-height: 34px; font-style: normal;
    color: var(--text-muted);
  }
  .contact-list { list-style: none; margin-top: 34px; }
  .contact-item {
    display: flex; align-items: center; gap: 12px;
    font-size: 27px; line-height: 36px;
    color: var(--text-muted);
  }
  .contact-icon { width: 30px; height: 30px; flex: none; }
  .brand-mark {
    position: absolute;
    left: 620px; top: 260px;
    width: 340px;
    display: flex; align-items: center; justify-content: center; gap: 16px;
  }
  .brand-dot {
    width: 26px; height: 26px; border-radius: 50%;
    background: var(--brand-ink);
  }
  .brand-name {
    font-size: 52px; font-weight: 900; letter-spacing: 3px;
    color: var(--brand-ink);
    text-transform: uppercase;
  }
</style>
</head>
<body>
  <div class="business-card">
    <svg class="card-shapes" width="1040" height="592" viewBox="0 0 1040 592" aria-hidden="true">
      <defs>
        <linearGradient id="panelFill" x1="0" y1="0" x2="0.3" y2="1">
          <stop offset="0" stop-color="var(--panel-top)"/>
          <stop offset="0.5" stop-color="var(--panel-mid)"/>
          <stop offset="1" stop-color="var(--panel-bottom)"/>
        </linearGradient>
      </defs>
      <path d="M0,0 H540 Q440,296 540,592 H0 Z" fill="url(#panelFill)"/>
      <path d="M528,40 Q470,296 534,592" fill="none" stroke="var(--silver)" stroke-width="3" opacity="0.8"/>
    </svg>

    <div class="contact-panel">
      <h1 class="holder-name">Derek Halloway</h1>
      <p class="holder-role">Owner</p>
      <address class="postal-address">
        PO Box 4127,<br>
        18 Cedar Mill Lane<br>
        Chesapeake, VA 23320
      </address>
      <ul class="contact-list">
        <li class="contact-item">
          <svg class="contact-icon" viewBox="0 0 30 30" aria-hidden="true">
            <circle cx="15" cy="15" r="13.5" fill="none" stroke="currentColor" stroke-width="2"/>
            <path d="M9 11 Q15 7 21 11 L20 13 L17.5 12.5 L17 11 H13 L12.5 12.5 L10 13 Z M11 15 H19 L21 21 H9 Z" fill="currentColor"/>
          </svg>
          <span>(757) 482-3175</span>
        </li>
        <li class="contact-item">
          <svg class="contact-icon" viewBox="0 0 30 30" aria-hidden="true">
            <circle cx="15" cy="15" r="13.5" fill="none" stroke="currentColor" stroke-width="2"/>
            <rect x="8" y="10" width="14" height="10" fill="currentColor"/>
            <path d="M8 10 L15 16 L22 10" fill="none" stroke="#2f3541" stroke-width="1.5"/>
          </svg>
          <span>derek@lumbrella-shop.example</span>
        </li>
        <li class="contact-item">
          <svg class="contact-icon" viewBox="0 0 30 30" aria-hidden="true">
            <circle cx="15" cy="15" r="13.5" fill="none" stroke="currentColor" stroke-width="2"/>
            <circle cx="15" cy="15" r="7.5" fill="none" stroke="currentColor" stroke-width="1.5"/>
            <ellipse cx="15" cy="15" rx="3.2" ry="7.5" fill="none" stroke="currentColor" stroke-width="1.2"/>
            <path d="M7.5 15 H22.5 M9 11 H21 M9 19 H21" stroke="currentColor" stroke-width="1.2"/>
          </svg>
          <span>lumbrella-shop.example</span>
        </li>
      </ul>
    </div>

    <div class="brand-mark">
      <span class="brand-dot"></span>
      <span class="brand-name">Lumbrella</span>
    </div>
  </div>
</body>
</html>
```